Boutique investment company is looking for money

We, Cardelith, are a very small boutique consulting and investment management firm in SWITZERLAND. Cardelith is trying to raise EUR 5-15 million in areas not easily accessible to private investors.

It will not be possible to raise these funds from traditional institutional investors because:
- Time and budget constraints
- Lack of track record in this particular area
Therefore, the capital has to be raised from in a non-conventional way, guerilla-style, from probably 10-15 private investors providing 1 million each. What can we offer? First, the money will be in Switzerland. Second, it will not be with a large bank – so, discretion is guaranteed. We are no-bullshit but data-driven, out of the box investors. We are different.

The site is only the bait to contact us. Maybe it should look like a presentation, just with additional elements for navigation. Maybe there should be one image or a chart explaining each page.

The site will be small, five pages, in two or three languages each.

Investors in Russia and South America

Boutique

Coded - Design and coding required

4 page

• Read the "Nice to Haves" section

Requirements
Must have
• If you have local insight to Russia and Southern America - use it.
• I am German and I love modern architecture - and I would like to see simple and logical design, including easy navigation.
• I am enclosing some files you may find useful. The graphics need to be consistent and can either be clean like they are now or look improvised and hand-drawn - if you can turn them consistently into that.
• We need a home page that should simply state "Safe, secure, Swiss" and then four pages: About Cardelith, Investment opportunity, Absolute return investing,
• Investment strategy. And the navigation needs to allow to toggle between English, Russian and Spanish.
• Let me help you by providing some examples of the kind of site that I have in mind, crisp, clean, simple (the sites are listed in alphabetical order):
• vemoridge.example
• tulsenfield.example
• quorvanholt.example
• zepharlind.example
• dormivelleco.example
• ketraholm.example
• lurovaspring.example
• pelmorath.example
• wistegrove.example
• fendralwick.example
• orbesquay.example
• jyn-halcrest.example
• Take a look at these and your job will become easier, much easier. They all have the same type of look and feel to them.
• One really cool landing page is here:
• wdlt.example
• Maybe we can do something like on their landing page in our logo with ursae minoris (see pictures)?
• If you use pictures, think Switzerland. Google the following and look at images:
• Matterhorn
• luzern vierwaldstättersee
• mechanical swiss watch
• vault
Nice to have
• Please look at the logo. I like the Sans Serif Fonts, Gill Sans and Helvetica Neue above all. Colors based on the logo are:
• - dark blue R: 0, G: 22, B: 115
• - light blue R: 68, G: 133, B: 212
Should not have
• Unless you feel that the audience loves pompous design, let's keep it straight.

```html
<!DOCTYPE html>
<html lang="en">
<head>
<meta charset="utf-8">
<title>Cardelith – Safe, Secure, Swiss</title>
<link rel="stylesheet" href="https://fonts.googleapis.com/css2?family=Open+Sans:ital,wght@0,400;0,600;0,700;1,600;1,700&display=swap">
<style>
:root{
  --navy:#00166f;
  --deep:#0b2159;
  --blue:#4485d4;
  --nav:#3b78c9;
  --nav-active:#1c4f9c;
  --band-top:#3f7dcf;
  --band-bottom:#6fa3e0;
  --ink:#333a45;
  --muted:#7a828e;
  --rule:#dfe3e8;
  --white:#ffffff;
  --foot:#0d2150;
  --foot-text:#b9c4d8;
}
*{box-sizing:border-box;margin:0;padding:0}
html,body{width:1200px;height:2200px;overflow:hidden;background:var(--white);font-family:"Open Sans",Arial,sans-serif;color:var(--ink)}
.page{position:relative;width:1200px;height:2200px;overflow:hidden}
a{color:inherit;text-decoration:none}

/* header */
.header{position:absolute;top:0;left:0;width:1200px;height:170px;background:var(--white)}
.brand{position:absolute;left:24px;top:38px;display:flex;align-items:center;gap:12px}
.brand-dot{width:44px;height:44px;border-radius:50%;background:var(--blue)}
.brand-name{font-size:34px;font-weight:700;color:var(--navy);letter-spacing:.5px}
.lang{position:absolute;right:40px;top:22px;width:120px;height:26px;border:1px solid var(--rule);font-size:12px;display:flex;align-items:center;padding:0 10px;gap:8px;color:var(--muted)}
.lang-flag{width:14px;height:10px;background:#c0392b}
.lang-caret{margin-left:auto;font-size:9px}
.nav{position:absolute;left:80px;top:126px;width:1100px;height:40px;background:var(--nav);display:flex}
.nav a{color:var(--white);font-size:13px;font-weight:600;letter-spacing:.6px;padding:0 24px;line-height:40px;white-space:nowrap}
.nav a.active{background:var(--nav-active)}

/* hero */
.hero{position:absolute;top:170px;left:0;width:1200px;height:630px;background:linear-gradient(180deg,#9fc4ea 0%,#5d8fc8 45%,#2d5d9a 75%,#c79a63 100%)}
.hero-title{position:absolute;left:0;width:100%;top:470px;text-align:center;color:var(--white);font-size:44px;font-weight:600;letter-spacing:3px;text-shadow:0 2px 6px rgba(0,0,0,.35)}
.hero-arrow{position:absolute;top:300px;width:36px;height:36px;border-radius:50%;background:rgba(0,0,0,.55)}
.hero-arrow.left{left:34px}.hero-arrow.right{right:34px}
.hero-arrow svg{width:36px;height:36px}

/* features */
.features{position:absolute;top:840px;left:80px;width:1040px;display:flex;justify-content:space-between}
.feature{width:320px;display:flex;gap:18px}
.feature-icon{flex:none;width:62px;height:62px;border-radius:50%;border:2px solid var(--blue);display:flex;align-items:center;justify-content:center}
.feature h3{font-size:19px;font-weight:700;color:var(--deep);letter-spacing:.8px;margin:4px 0 10px}
.feature p{font-size:12.5px;line-height:1.55;color:var(--muted)}
.more{display:inline-block;margin-top:10px;font-size:12px;font-weight:700;color:var(--blue);letter-spacing:.5px}

/* welcome band */
.welcome{position:absolute;top:1040px;left:0;width:1200px;height:600px;background:linear-gradient(180deg,var(--band-top),var(--band-bottom))}
.welcome h2{position:absolute;left:100px;top:46px;font-size:40px;font-weight:700;color:var(--white);letter-spacing:1px}
.welcome-text{position:absolute;left:100px;top:112px;width:1000px;font-size:13px;line-height:1.7;color:#e6efff}
.btn-dark{position:absolute;left:100px;top:192px;background:var(--deep);color:var(--white);font-size:12px;font-weight:700;letter-spacing:1px;padding:9px 18px}
.cards{position:absolute;left:100px;top:268px;width:1000px;display:flex;justify-content:space-between}
.card{width:300px;text-align:center}
.card-photo{width:300px;height:156px;background:linear-gradient(135deg,#d9e3ee,#8aa1bb)}
.card h3{margin-top:26px;font-size:16px;font-weight:700;color:var(--white);letter-spacing:1px}
.card p{margin-top:8px;font-size:12px;line-height:1.55;color:#e6efff}
.card .more{color:var(--white)}

/* news */
.news{position:absolute;top:1670px;left:80px;width:1040px}
.news-head{display:flex;align-items:center;border-bottom:1px solid var(--rule);padding-bottom:14px}
.news-head h2{font-size:34px;font-weight:700;color:var(--deep);letter-spacing:1px}
.news-arrows{margin-left:auto;display:flex;gap:4px}
.news-arrows span{width:26px;height:26px;background:#8a929c;display:flex;align-items:center;justify-content:center}
.news-list{display:flex;justify-content:space-between;margin-top:24px}
.news-item{width:320px}
.news-date{display:flex;align-items:center;gap:8px;font-size:17px;font-weight:700;color:var(--blue);padding-bottom:10px;border-bottom:1px solid var(--rule)}
.news-item h3{margin-top:14px;font-size:15px;font-style:italic;font-weight:700;color:var(--deep);line-height:1.4}
.news-item p{margin-top:10px;font-size:12.5px;line-height:1.55;color:var(--muted)}

/* footer */
.footer{position:absolute;top:1990px;left:0;width:1200px;height:210px;background:var(--foot);color:var(--foot-text);font-size:12px}
.foot-col{position:absolute;top:22px}
.foot-col h4{font-size:17px;font-weight:700;color:var(--white);letter-spacing:1px;margin-bottom:12px}
.foot-col li{list-style:none;line-height:1.7;display:flex;align-items:center;gap:8px}
.foot-col p{line-height:1.6}
.bullet{width:5px;height:5px;background:var(--blue);border-radius:50%}
.soc{width:12px;height:12px;background:var(--blue)}
.btn-signup{display:inline-block;margin-top:14px;background:var(--blue);color:var(--white);font-weight:700;font-size:12px;letter-spacing:1px;padding:8px 24px}
</style>
</head>
<body>
<div class="page">

  <header class="header">
    <div class="brand"><span class="brand-dot"></span><span class="brand-name">Cardelith</span></div>
    <div class="lang"><span class="lang-flag"></span>ENGLISH<span class="lang-caret">▼</span></div>
    <nav class="nav">
      <a class="active">HOME</a>
      <a>ABOUT CARDELITH</a>
      <a>INVESTMENT OPPORTUNITY</a>
      <a>ABSOLUTE RETURN INVESTING</a>
      <a>INVESTMENT STRATEGY</a>
      <a>CONTACT US</a>
    </nav>
  </header>

  <section class="hero" role="img" aria-label="Photograph of modern glass skyscrapers against a blue sky with a bridge in the foreground">
    <span class="hero-arrow left"><svg viewBox="0 0 36 36"><path d="M21 11l-7 7 7 7" fill="none" stroke="#fff" stroke-width="2.5"/></svg></span>
    <span class="hero-arrow right"><svg viewBox="0 0 36 36"><path d="M15 11l7 7-7 7" fill="none" stroke="#fff" stroke-width="2.5"/></svg></span>
    <h1 class="hero-title">SAFE, SECURE, SWISS</h1>
  </section>

  <section class="features">
    <div class="feature">
      <div class="feature-icon"><svg width="30" height="26" viewBox="0 0 30 26"><rect x="2" y="7" width="26" height="17" rx="2" fill="none" stroke="#4485d4" stroke-width="2"/><path d="M10 7V3h10v4" fill="none" stroke="#4485d4" stroke-width="2"/></svg></div>
      <div><h3>PRAESENT VESTIB</h3><p>Lorem ipsum dolor sit amet, consectetuer adipiscing elit. Praese vestibulum molestie.</p><a class="more">READ MORE</a></div>
    </div>
    <div class="feature">
      <div class="feature-icon"><svg width="28" height="28" viewBox="0 0 28 28"><circle cx="14" cy="14" r="5" fill="none" stroke="#4485d4" stroke-width="2"/><path d="M14 2v5M14 21v5M2 14h5M21 14h5M5.5 5.5l3.5 3.5M19 19l3.5 3.5M5.5 22.5L9 19M19 9l3.5-3.5" stroke="#4485d4" stroke-width="2"/></svg></div>
      <div><h3>NEQUE PORRO</h3><p>Lorem ipsum dolor sit amet, consectetuer adipiscing elit. Praese vestibulum molestie.</p><a class="more">READ MORE</a></div>
    </div>
    <div class="feature">
      <div class="feature-icon"><svg width="28" height="28" viewBox="0 0 28 28"><path d="M3 23l7-8 5 5 10-12" fill="none" stroke="#4485d4" stroke-width="2"/><path d="M3 3v22h22" fill="none" stroke="#4485d4" stroke-width="2"/></svg></div>
      <div><h3>SED UT PERSPICIA</h3><p>Lorem ipsum dolor sit amet, consectetuer adipiscing elit. Praese vestibulum molestie.</p><a class="more">READ MORE</a></div>
    </div>
  </section>

  <section class="welcome">
    <h2>WELCOME!</h2>
    <p class="welcome-text">Cardelith Advisors AG ("Cardelith") is a boutique investment management and consulting firm focusing on absolute return investment strategies in collateralised markets. It was incorporated in Switzerland with a modest share capital and is led by a founder with long experience in markets and entrepreneurship.</p>
    <a class="btn-dark">LEARN MORE</a>
    <div class="cards">
      <div class="card">
        <div class="card-photo" role="img" aria-label="Photograph of business people meeting around a table"></div>
        <h3>BUSINESS PRACTICE</h3>
        <p>Lorem ipsum dolor sit amet, consectetuer<br>adipiscing elit. Praesent vesti.</p>
        <a class="more">LEARN MORE</a>
      </div>
      <div class="card">
        <div class="card-photo" role="img" aria-label="Photograph of a team of colleagues in an office"></div>
        <h3>TEAM WORK</h3>
        <p>Lorem ipsum dolor sit amet, consectetuer<br>adipiscing elit. Praesent vesti.</p>
        <a class="more">LEARN MORE</a>
      </div>
      <div class="card">
        <div class="card-photo" role="img" aria-label="Photograph of a professional working at a desk"></div>
        <h3>CAREERS</h3>
        <p>Lorem ipsum dolor sit amet, consectetuer<br>adipiscing elit. Praesent vesti.</p>
        <a class="more">LEARN MORE</a>
      </div>
    </div>
  </section>

  <section class="news">
    <div class="news-head">
      <h2>NEWS &amp; EVENTS</h2>
      <div class="news-arrows">
        <span><svg width="10" height="12" viewBox="0 0 10 12"><path d="M7 1L2 6l5 5" fill="none" stroke="#fff" stroke-width="2"/></svg></span>
        <span><svg width="10" height="12" viewBox="0 0 10 12"><path d="M3 1l5 5-5 5" fill="none" stroke="#fff" stroke-width="2"/></svg></span>
      </div>
    </div>
    <div class="news-list">
      <article class="news-item">
        <div class="news-date"><svg width="18" height="18" viewBox="0 0 18 18"><rect x="1.5" y="3" width="15" height="13.5" fill="none" stroke="#4485d4" stroke-width="1.8"/><path d="M1.5 7h15M5 1v4M13 1v4" stroke="#4485d4" stroke-width="1.8"/></svg>12/08/2015</div>
        <h3>Aenean nonummy hendrerit mauris phasellus porta fusce</h3>
        <p>Lorem ipsum dolor sit amet, consectetuer adipiscing elit. Praesent vestibulum molestie lacus. Aenean nonummy.</p>
        <a class="more">READ MORE</a>
      </article>
      <article class="news-item">
        <div class="news-date"><svg width="18" height="18" viewBox="0 0 18 18"><rect x="1.5" y="3" width="15" height="13.5" fill="none" stroke="#4485d4" stroke-width="1.8"/><path d="M1.5 7h15M5 1v4M13 1v4" stroke="#4485d4" stroke-width="1.8"/></svg>12/08/2015</div>
        <h3>Aenean nonummy hendrerit mauris phasellus porta fusce</h3>
        <p>Lorem ipsum dolor sit amet, consectetuer adipiscing elit. Praesent vestibulum molestie lacus. Aenean nonummy.</p>
        <a class="more">READ MORE</a>
      </article>
      <article class="news-item">
        <div class="news-date"><svg width="18" height="18" viewBox="0 0 18 18"><rect x="1.5" y="3" width="15" height="13.5" fill="none" stroke="#4485d4" stroke-width="1.8"/><path d="M1.5 7h15M5 1v4M13 1v4" stroke="#4485d4" stroke-width="1.8"/></svg>12/08/2015</div>
        <h3>Aenean nonummy hendrerit mauris phasellus porta fusce</h3>
        <p>Lorem ipsum dolor sit amet, consectetuer adipiscing elit. Praesent vestibulum molestie lacus. Aenean nonummy.</p>
        <a class="more">READ MORE</a>
      </article>
    </div>
  </section>

  <footer class="footer">
    <div class="foot-col" style="left:80px">
      <h4>GET IN TOUCH</h4>
      <p>14 Lindenhof Lane<br>Zurich, CH 8001</p>
      <p style="margin-top:8px">Freephone: +1 800 555 0100<br>Telephone: +1 800 555 0101<br>Fax: +1 800 555 0102<br>E-mail: mail@cardelith.example</p>
    </div>
    <div class="foot-col" style="left:340px">
      <h4>USEFUL LINKS</h4>
      <ul><li><span class="bullet"></span>About us</li><li><span class="bullet"></span>Solutions</li><li><span class="bullet"></span>Services</li><li><span class="bullet"></span>Projects</li><li><span class="bullet"></span>Clients</li><li><span class="bullet"></span>Contacts</li></ul>
    </div>
    <div class="foot-col" style="left:560px">
      <h4>FOLLOW US</h4>
      <ul><li><span class="soc"></span>Linkvale</li><li><span class="soc"></span>Chirpline</li><li><span class="soc"></span>Streamora</li><li><span class="soc"></span>RSS</li></ul>
    </div>
    <div class="foot-col" style="left:820px;width:300px">
      <h4>JOIN OUR NEWSLETTER</h4>
      <p>And always stay informed of the latest company news and events!</p>
      <a class="btn-signup">SIGN UP</a>
    </div>
  </footer>

</div>
</body>
</html>
```